Standout Plastic Packaging for a Natural Air Purifying Product!

Hello, we are Ferndale Living Co. and this packaging design will be for our multipurpose 8-pack of Natural Air Purifiers.

We are listing our products for sale online, and its a very crowded marketplace, so we are looking for a stand-out, colourful, on-brand approach to our packaging design.

- Refer to "design template for package" file for actual template of packaging to be printed. We cannot do any other size; final design must be on this template provided.

- We would like the front of our packaging to be an extended version of our logo design; so I have attached AI logo files to make this happen.

- We are aiming for a minimalistic, symmetrical, on-brand design to host our premium homeware brand designed for American's.

- Refer to the "MOCKUP_front" and "MOCKUP_back" files for all of the preferred text, colours, and overall concept we have in mind.

Looking forward to seeing your ideas! :)

BRAND COLOUR CODES:
#e7948a
#f8b195
#f3e1d8
#f67280
#c06c84
#6c5b7b
#355c7d
#274357

BRAND FONTS:
Raleway
Quickbrush
Sifonn Outline
Montserrat

Currently on holidays, apologies for slow replies

Target Market(s)

Bazaro shoppers, women aged 27-55, located in the USA

Font styles to use
Other font styles liked:
• Raleway, Quickbrush, Sifonn Outline, Montserrat

Requirements
Must have
• - Brand colours (see project description)
• - Extend logo to suit packaging template provided
• - Refer to front and back mockup files attached
• - Minimal & symmetrical design
• - Symbol for 8 PACK
• - Space for barcode on rear
Nice to have
• Refer to mockup file attached

```html
<!DOCTYPE html>
<html lang="en">
<head>
<meta charset="UTF-8">
<title>Ferndale Living Co. – Natural Air Purifiers Packaging</title>
<link rel="stylesheet" href="https://fonts.googleapis.com/css2?family=Montserrat:wght@400;500;600;700&family=Raleway:wght@400;500&display=swap">
<style>
  :root {
    --salmon: #e7948a;
    --peach: #f8b195;
    --blush: #f3e1d8;
    --coral: #f67280;
    --rose: #c06c84;
    --plum: #6c5b7b;
    --slate: #355c7d;
    --navy: #274357;
    --ink: #3a3342;
    --backdrop: #e6ecec;
    --muted: #5c6470;
  }
  * { box-sizing: border-box; margin: 0; padding: 0; }
  html, body { width: 1200px; height: 1200px; overflow: hidden; }
  body {
    position: relative;
    background: var(--backdrop);
    font-family: "Montserrat", sans-serif;
    color: var(--ink);
  }
  .pouch {
    position: absolute;
    top: 212px;
    width: 532px;
    height: 692px;
    background: var(--blush);
    border-radius: 10px 10px 4px 4px;
    overflow: hidden;
    box-shadow: 0 14px 30px rgba(39, 67, 87, 0.12);
  }
  .pouch--front { left: 52px; }
  .pouch--back { left: 616px; }
  .pouch__band {
    position: absolute; left: 0; top: 0; width: 100%; height: 172px;
    background: linear-gradient(180deg, #3d5a70 0%, var(--slate) 55%, #3f6179 100%);
  }
  .pouch__window {
    position: absolute; left: 154px; top: -4px; width: 224px; height: 224px;
    border-radius: 50%;
  }
  .pouch__window--scene {
    background: linear-gradient(180deg, #f6d8d0 0%, #f4b8a6 38%, var(--salmon) 52%, var(--rose) 66%, var(--plum) 76%, var(--slate) 88%, var(--navy) 100%);
  }
  .pouch__window--charcoal {
    background: radial-gradient(circle at 40% 40%, #8a8589 0%, #4a4649 45%, #2a2729 100%);
  }
  .abs { position: absolute; left: 0; width: 100%; text-align: center; }

  /* front */
  .brand-name { top: 262px; font-size: 36px; font-weight: 500; color: var(--ink); letter-spacing: 0.04em; }
  .product-title { top: 378px; font-size: 27px; font-weight: 500; color: var(--coral); letter-spacing: 0.08em; }
  .material-rule { position: absolute; left: 82px; width: 368px; height: 1px; background: var(--navy); }
  .material-rule--top { top: 422px; }
  .material-rule--bottom { top: 454px; }
  .material { top: 427px; font-size: 20px; font-weight: 700; color: var(--slate); letter-spacing: 0.1em; }
  .feature { position: absolute; top: 476px; width: 120px; text-align: center; }
  .feature__icon {
    width: 50px; height: 50px; margin: 0 auto; border: 1.5px solid var(--slate);
    border-radius: 50%; display: flex; align-items: center; justify-content: center;
    color: var(--slate);
  }
  .feature__years { font-size: 17px; font-weight: 700; line-height: 1; }
  .feature__years small { display: block; font-size: 6px; letter-spacing: 0.08em; font-weight: 600; }
  .feature__label { margin-top: 14px; font-size: 11px; font-weight: 500; letter-spacing: 0.1em; color: var(--slate); }
  .feature--natural { left: 95px; }
  .feature--pet { left: 205px; }
  .feature--reuse { left: 315px; }
  .pack-badge {
    position: absolute; left: 152px; top: 564px; width: 228px; height: 48px;
    background: linear-gradient(90deg, var(--navy), var(--slate), var(--navy));
    border-radius: 3px; display: flex; align-items: center; justify-content: center;
    font-size: 26px; font-weight: 700; color: var(--coral); letter-spacing: 0.08em;
  }
  .pack-contents { top: 624px; font-size: 12px; line-height: 1.35; letter-spacing: 0.06em; color: var(--navy); }
  .pack-contents strong { font-weight: 500; }

  /* back */
  .back-title { top: 240px; font-size: 26px; font-weight: 500; color: var(--ink); letter-spacing: 0.1em; }
  .back-tagline { top: 278px; font-size: 12px; font-weight: 500; color: var(--rose); letter-spacing: 0.1em; }
  .back-claims { top: 305px; font-size: 11px; font-weight: 600; line-height: 1.6; color: var(--navy); letter-spacing: 0.1em; }
  .back-list { top: 345px; font-family: "Raleway", sans-serif; font-size: 11.5px; line-height: 1.25; color: var(--muted); letter-spacing: 0.1em; }
  .back-rule { position: absolute; left: 87px; width: 370px; height: 2px; background: var(--rose); opacity: 0.8; }
  .back-rule--top { top: 431px; }
  .back-rule--bottom { top: 566px; }
  .back-heading { font-size: 12.5px; font-weight: 600; color: var(--rose); letter-spacing: 0.1em; }
  .back-heading--inside { top: 446px; }
  .back-heading--support { top: 516px; }
  .back-copy { font-family: "Raleway", sans-serif; font-size: 12.5px; line-height: 1.3; color: var(--muted); letter-spacing: 0.06em; }
  .back-copy--inside { top: 469px; }
  .back-copy--support { top: 541px; }
  .social { position: absolute; left: 98px; top: 592px; width: 150px; text-align: center; }
  .social__dots { display: flex; justify-content: center; gap: 10px; }
  .social__dot { width: 36px; height: 36px; border-radius: 50%; background: var(--slate); }
  .social__handle { margin-top: 6px; font-size: 12px; color: var(--navy); font-family: "Raleway", sans-serif; }
  .origin { position: absolute; left: 330px; top: 650px; width: 230px; text-align: center; font-size: 9px; line-height: 1.4; color: var(--muted); }
</style>
</head>
<body>

<section class="pouch pouch--front" aria-label="Front of pouch">
  <div class="pouch__band"></div>
  <div class="pouch__window pouch__window--scene" role="img" aria-label="Layered mountain range at sunrise in peach, rose and blue tones"></div>
  <div class="abs brand-name">Ferndale Living Co.</div>
  <div class="abs product-title">NATURAL AIR PURIFIERS</div>
  <div class="material-rule material-rule--top"></div>
  <div class="abs material">100% BAMBOO CHARCOAL</div>
  <div class="material-rule material-rule--bottom"></div>

  <div class="feature feature--natural">
    <div class="feature__icon">
      <svg width="28" height="24" viewBox="0 0 28 24" aria-hidden="true">
        <path d="M14 22 C6 20 3 12 5 4 C11 6 14 12 14 22Z" fill="currentColor"/>
        <path d="M14 22 C22 20 25 12 23 4 C17 6 14 12 14 22Z" fill="none" stroke="currentColor" stroke-width="1.5"/>
      </svg>
    </div>
    <div class="feature__label">NATURAL</div>
  </div>
  <div class="feature feature--pet">
    <div class="feature__icon">
      <svg width="28" height="26" viewBox="0 0 28 26" aria-hidden="true" fill="currentColor">
        <ellipse cx="6" cy="10" rx="3" ry="4"/>
        <ellipse cx="11" cy="5" rx="3" ry="4"/>
        <ellipse cx="17" cy="5" rx="3" ry="4"/>
        <ellipse cx="22" cy="10" rx="3" ry="4"/>
        <path d="M14 25 L7 18 C5 15 8 12 11 13 L14 15 L17 13 C20 12 23 15 21 18Z"/>
      </svg>
    </div>
    <div class="feature__label">PET FRIENDLY</div>
  </div>
  <div class="feature feature--reuse">
    <div class="feature__icon"><div class="feature__years">2<small>YEARS</small></div></div>
    <div class="feature__label">REUSEBLE</div>
  </div>

  <div class="pack-badge">8 PACK</div>
  <div class="abs pack-contents"><strong>Multipurpose Pack Includes:</strong><br>1 x 500g, 2 x 200g, 1 x 100g, 4 x 50g</div>
</section>

<section class="pouch pouch--back" aria-label="Back of pouch">
  <div class="pouch__band"></div>
  <div class="pouch__window pouch__window--charcoal" role="img" aria-label="Close view of bamboo charcoal pieces"></div>
  <div class="abs back-title">100% BAMBOO CHARCOAL</div>
  <div class="abs back-tagline">SAFE ALTERNATIVE TO HARMFUL AIR FRESHENER SPRAYS</div>
  <div class="abs back-claims">PRODUCES HEALTY &amp; PURIFIED AIR<br>ABSORB &amp; ELIMINATES IMPURITIES</div>
  <div class="abs back-list">HARMFUL TOXINS<br>ORDORS<br>MOISTURE<br>MOLD &amp; MILDEW<br>ALLERGENS</div>
  <div class="back-rule back-rule--top"></div>
  <div class="abs back-heading back-heading--inside">SEE INSIDE FOR:</div>
  <div class="abs back-copy back-copy--inside">Instructions on where to use, how to reuse for up to 2 years,<br>and how to claim your extended 2 year warranty.</div>
  <div class="abs back-heading back-heading--support">NEED SUPPORT?</div>
  <div class="abs back-copy back-copy--support">Email us at yourexperience@ferndalelivingco.shop</div>
  <div class="back-rule back-rule--bottom"></div>
  <div class="social">
    <div class="social__dots"><span class="social__dot"></span><span class="social__dot"></span></div>
    <div class="social__handle">@ferndalelivingco</div>
  </div>
  <div class="origin">Ferndale inspired. Made in China.<br>X oz</div>
</section>

</body>
</html>
```